Letterhead for Midwest Law Firm

Our law firm does estate planning and trust administration in Wisconsin and Illinois. We recently obtained a new logo and need to incorporate it into new stationary. The stationary needs to list out the attorneys at the firm, but we will want 3 variations, one with three attorneys, one with six, and one with six plus the names of states where each is licensed to practice (possibly as an asterisk with notation somewhere towards bottom of page. As with most traditional law practices, letterhead should be conservative and convey predictability and reliability. We view our brand as being primarily reliability, with prestige as a secondary element. We are upmarket, but would like to avoid seeming pretentious or "slick". We are a smaller firm with a personal touch.

Target Market(s)

Affluent Midwestern Americans approaching at or approaching retirement age.

Industry/Entity Type

Legal

Font styles to use
Serif
Sans Serif

Requirements
Must have
• Must use our logo. Must comply with Brennick Legal Guild Ethics rules: https://www.halvorjudic.org/courts/offices/docs/pqmtnv20annotated.pdf. Must be conventional. Must list names of attorneys and provide contact information for firm. Note that we are asking for three designs with very minor variations. Also, designer must provide letterhead in a format that is industry-standard for stationary printers.
Nice to have
• We would appreciate an alternate version that will look reasonable when printed on a black-and-white printer. Designer can use judgment as to whether to have use grayscale, black/white, or something in between.
Should not have
• No "motto" or "visit our website" extraneous materials. putting the website address somewhere is fine, but overall there is a lot of required text, and we'd like to not appear cluttered.

```html
<!DOCTYPE html>
<html lang="en">
<head>
<meta charset="utf-8">
<title>Holloway &amp; Brandt LLP — Letterhead</title>
<link rel="stylesheet" href="https://fonts.googleapis.com/css2?family=EB+Garamond:ital,wght@0,400;0,500;0,600;1,400&display=swap">
<style>
  :root {
    --backdrop: #a7a8ac;
    --paper: #ffffff;
    --ink: #2b2a3d;
    --accent-color: #f0ac29;
    --accent-mono: #b9babc;
  }
  * { margin: 0; padding: 0; box-sizing: border-box; }
  html, body {
    width: 1200px;
    height: 839px;
    overflow: hidden;
    background: var(--backdrop);
  }
  .board {
    position: relative;
    width: 1200px;
    height: 839px;
  }
  .sheet {
    position: absolute;
    width: 503px;
    height: 711px;
    background: var(--paper);
    color: var(--ink);
    font-family: "EB Garamond", Garamond, serif;
  }
  .sheet--color { left: 69px; top: 65px; --accent: var(--accent-color); }
  .sheet--mono  { left: 636px; top: 66px; --accent: var(--accent-mono); }

  .firm-mark {
    position: absolute;
    left: 48px;
    top: 36px;
    display: flex;
    align-items: center;
    gap: 10px;
  }
  .firm-mark__dot {
    width: 30px;
    height: 30px;
    border-radius: 50%;
    background: var(--accent);
  }
  .firm-mark__name {
    font-weight: 600;
    font-size: 16px;
    letter-spacing: 0.2px;
    color: var(--ink);
  }

  .attorneys {
    position: absolute;
    left: 342px;
    top: 21px;
    list-style: none;
  }
  .attorneys li {
    font-size: 8.8px;
    line-height: 17.8px;
    letter-spacing: 0.1px;
    white-space: nowrap;
  }
  .attorneys .role { font-style: italic; }

  .contact {
    position: absolute;
    left: 0;
    right: 0;
    top: 664px;
    text-align: center;
    font-style: italic;
    font-size: 10.6px;
    line-height: 12.4px;
    white-space: nowrap;
  }
  .contact .sep {
    display: inline-block;
    width: 4px;
    height: 4px;
    margin: 0 8px 1px;
    border-radius: 50%;
    background: var(--accent);
    vertical-align: middle;
  }
</style>
</head>
<body>
<main class="board">

  <section class="sheet sheet--color" aria-label="Letterhead, colour version">
    <header class="firm-mark">
      <span class="firm-mark__dot"></span>
      <span class="firm-mark__name">Holloway &amp; Brandt LLP</span>
    </header>
    <ul class="attorneys">
      <li>DANIEL P. HOLLOWAY, <span class="role">Attorney</span></li>
      <li>THOMAS E. BRANDT, <span class="role">Attorney</span></li>
      <li>GREGORY L. WESTCOTT, <span class="role">Attorney</span></li>
    </ul>
    <footer class="contact">
      <p>275 West Larkin Avenue, Suite 300<span class="sep"></span>Millbrook, Wisconsin 53999</p>
      <p>Telephone: 555-013-4200<span class="sep"></span>FAX: 555-013-2781<span class="sep"></span>Website: www.hollowaybrandtllp.com</p>
    </footer>
  </section>

  <section class="sheet sheet--mono" aria-label="Letterhead, grayscale version">
    <header class="firm-mark">
      <span class="firm-mark__dot"></span>
      <span class="firm-mark__name">Holloway &amp; Brandt LLP</span>
    </header>
    <ul class="attorneys">
      <li>DANIEL P. HOLLOWAY, <span class="role">Attorney</span></li>
      <li>THOMAS E. BRANDT, <span class="role">Attorney</span></li>
      <li>GREGORY L. WESTCOTT, <span class="role">Attorney</span></li>
    </ul>
    <footer class="contact">
      <p>275 West Larkin Avenue, Suite 300<span class="sep"></span>Millbrook, Wisconsin 53999</p>
      <p>Telephone: 555-013-4200<span class="sep"></span>FAX: 555-013-2781<span class="sep"></span>Website: www.hollowaybrandtllp.com</p>
    </footer>
  </section>

</main>
</body>
</html>
```